Flyer Design für Berater
Zielgruppe
Beratung für kleinere Unternehmen (z.B. KMUs, Stiftungen, Verbände)
intern bei Grossunternehmen
Aufgabenstellung
Schlichtes Design, Fraben türkis - blau
zu 70% als digitales pdf zu verwenden, zu 30 % als print

```html
<!DOCTYPE html>
<html lang="de">
<head>
<meta charset="utf-8">
<title>Flyer Beratung – Dreiteiler</title>
<link href="https://fonts.googleapis.com/css2?family=Quicksand:wght@300;400;500&family=Ubuntu:wght@500;700&display=swap" rel="stylesheet">
<style>
:root{
  --teal:#2f7f95;
  --teal-text:#2b7a93;
  --ink:#3b3b3b;
  --label:#b9b9b9;
  --accent:#c9c36a;
  --paper:#ffffff;
}
*{margin:0;padding:0;box-sizing:border-box}
html,body{width:1200px;height:372px;overflow:hidden;background:var(--paper)}
body{position:relative;font-family:"Quicksand",sans-serif;color:var(--ink)}
.abs{position:absolute}
.side-label{top:12px;font:300 24px/1 "Quicksand",sans-serif;color:var(--label);text-align:center;width:300px}
.h-display{font-family:"Ubuntu",sans-serif;font-weight:700;color:var(--teal-text);letter-spacing:.2px}
.body{font-size:4.1px;line-height:1.25;color:#444}
.body p{margin-bottom:3px}
.band{height:18px;background:var(--teal);color:#fff;font:700 9.6px/18px "Ubuntu",sans-serif;padding-left:18px;letter-spacing:.3px}
.offer-head{font:700 5px/1 "Ubuntu",sans-serif;color:#333}
.offer-title{font:700 4.6px/1.2 "Ubuntu",sans-serif;color:var(--teal-text)}
.icon{border-radius:50%;background:var(--accent)}
.icon.sq{border-radius:2px;background:#d9d9d9}
ul.body{list-style:none}
ul.body li::before{content:"• "}
/* front */
.front-photo{left:0;top:72px;width:300px;height:300px;background:linear-gradient(180deg,#e9b87a 0%,#c9c59a 22%,#9fb7a8 40%,#7a9a5c 58%,#8faa3c 80%,#a7b83a 100%)}
.front-head{left:0;top:105px;width:282px;height:43px;background:rgba(255,255,255,.88);padding:5px 0 0 25px;font-size:14.2px;line-height:1.2}
.front-text{left:25px;top:256px;width:252px;color:#fff}
.front-foot{left:18px;top:312px;width:282px;height:35px;background:rgba(255,255,255,.88);text-align:right;padding:5px 26px 0 0;font-size:10.4px;line-height:1.25}
/* back */
.back-photo{left:900px;top:72px;width:300px;height:300px;background:linear-gradient(180deg,#3f6fb6 0%,#7d9ed0 30%,#b9c6d4 55%,#8e8c78 72%,#4f6a3a 100%)}
.back-head{left:900px;top:90px;width:282px;height:20px;background:rgba(255,255,255,.9);padding-left:18px;font-size:9.6px;line-height:20px}
.back-text{color:#fff}
.contact{left:918px;top:300px;width:264px;height:54px;background:rgba(255,255,255,.9)}
.contact-lines{right:50px;top:6px;text-align:right;font:500 6px/1.35 "Ubuntu",sans-serif;color:var(--teal-text)}
.contact-lines b{color:#23495a}
.brand{right:4px;top:5px;width:40px;height:43px;border:1px solid #cfd9de;display:flex;align-items:flex-end;justify-content:center;font:700 14px/1 "Ubuntu",sans-serif;color:#23495a;padding-bottom:3px}
</style>
</head>
<body>
<div class="abs side-label" style="left:0">Vorderseite</div>
<div class="abs side-label" style="left:450px">Innen</div>
<div class="abs side-label" style="left:900px">Rückseite</div>

<!-- Vorderseite -->
<section class="front">
  <div class="abs front-photo" role="img" aria-label="Fluss in Abendsonne mit Bäumen und Wiese"></div>
  <h1 class="abs front-head h-display">WANN WIRD DIE FAHRT<br>AUF EINEM FLUSS ZUM GENUSS?</h1>
  <div class="abs body front-text">
    <p>Eine Flussfahrt in einem Boot wird dann zum gelungenen Erlebnis, wenn von Anfang bis Ende alles passt. Dazu braucht es neben allgemeinem Grundwissen wie etwa über Wetterprognose oder Strömungsverhalten eine entsprechende Vorbereitung und eine gemeinsame Vorstellung über das Ziel einer Flussfahrt. Gibt es entlang der Route ein Wehr oder sonstige Hindernisse? Tückische Strömungsmuster? Wo sind die attraktiven Stellen zum Picknicken? Wo sind mögliche Ausstiegsstellen? Und wie viele Personen sind im Boot? Wer macht was, damit alles koordiniert abläuft?</p>
    <p>Nun kann bei einer Bootsfahrt jeder seinen Teil übernehmen, sich vorher informieren und sich dann einbringen. Oder sie können jemanden beauftragen, der weiss, worauf es ankommt und dem Unternehmen zum Erfolg verhilft.</p>
    <p>Mein Angebot ist es, Sie dabei zu unterstützen, den richtigen Weg mit Ihrem Unternehmen, Ihrer Organisation, Ihrer Abteilung zu finden, Ihre Projekte also zum Fliessen zu bringen.</p>
  </div>
  <h2 class="abs front-foot h-display">UND WAS MACHE ICH FÜR SIE,<br>DAMIT IHRE FLUSSFAHRT ZUM ERFOLG WIRD?</h2>
</section>

<!-- Innen links -->
<section class="inner-left">
  <div class="abs band" style="left:300px;top:90px;width:300px">UMGEBUNGSDYNAMIK ERFASSEN</div>
  <div class="abs body" style="left:318px;top:114px;width:147px">Unsere Gesellschaft wird immer komplexer und dynamischer. Es genügt nicht mehr, auf heutige Herausforderungen zu reagieren. Es müssen künftige Chancen und Potenziale frühzeitig erkannt und passende Antworten darauf gefunden werden. Gefragt sind massgeschneiderte, individuelle und kreative Lösungen mit möglichst bescheidenen Ressourcen.</div>
  <div class="abs" style="left:482px;top:115px;width:100px;height:56px;background:linear-gradient(180deg,#1f4a6a,#6fb3c6 45%,#2a5d7a)" role="img" aria-label="Brechende Welle"></div>
  <div class="abs offer-head" style="left:318px;top:172px">KONKRETE ANGEBOTE DAZU:</div>
  <div class="abs icon" style="left:318px;top:182px;width:24px;height:24px" role="img" aria-label="Symbol Stakeholder-Netzwerk"></div>
  <div class="abs offer-title" style="left:345px;top:183px">UMFRAGEN UND INTERVIEWS<br>MIT STAKEHOLDERN</div>
  <div class="abs body" style="left:318px;top:211px;width:125px">
    <p>Welche Bedürfnisse hat Ihr Umfeld hat bzw. wie nimmt es bestimmte Entwicklungen wahr? Wie nehmen Kunden, Mitarbeitende oder Mitglieder Ihre Organisation wahr?</p>
    <p>Ich unterstütze Sie durch die Planung und Realisierung von Umfragen, Interviews oder indem ich für Sie eine Internetrecherche durchführe. Ich liefere Ihnen die Ergebnisse, in Form von Fakten und Ideeninputs und diskutiere mit Ihnen mögliche Verwertungs- und Umsetzungsmassnahmen.</p>
  </div>
  <svg class="abs" style="left:457px;top:182px" width="26" height="24" viewBox="0 0 26 24" role="img" aria-label="Symbol Liniendiagramm"><path d="M2 1v21h23" fill="none" stroke="#555" stroke-width="1"/><polyline points="6,17 11,12 16,15 22,7" fill="none" stroke="#555" stroke-width=".8"/><circle cx="6" cy="17" r="2" fill="#e07b3a"/><circle cx="11" cy="12" r="2" fill="#e07b3a"/><circle cx="16" cy="15" r="2" fill="#e07b3a"/><circle cx="22" cy="7" r="2" fill="#e07b3a"/></svg>
  <div class="abs offer-title" style="left:485px;top:183px">INTERNETRECHERCHEN<br>UND STUDIEN</div>
  <div class="abs body" style="left:457px;top:211px;width:125px">
    <p>Gibt es Themen, wie z.B. neue Geschäftsmodelle, neue Dienstleistungen, neue Mitwerber, über die sie gerne mehr Informationen hätten. Suchen Sie Wissen und Grundlagen für mögliche neue Wege, Strategien, Projekte? Das möglichst schnell, ohne viel Zeit zu investieren?</p>
    <p>Ich gestalte Ihnen ein mögliches Forschungsdesign und liefere Ihnen die Ergebnisse (ob in Form einer Präsentation, eines Berichts mit vorgeschlagenen Massnahmen oder als Zahlenwerk. Abgestimmt auf Ihre Bedürfnisse</p>
  </div>
  <div class="abs band" style="left:300px;top:272px;width:300px">PERSPEKTIVEN SCHAFFEN</div>
  <div class="abs body" style="left:318px;top:297px;width:147px">
    <p>...aus der Informationsflut, aus der Datenmasse, aus den Schlagzeilen, aus den Kundenfeedbacks, aus den strategischen Vorgaben.</p>
  </div>
  <ul class="abs body" style="left:318px;top:311px;width:147px">
    <li>Über den Tellerrand blicken und Neues entdecken</li>
    <li>Mögliche strategische Optionen oder operative Verbesserungsmassnahmen erkennen</li>
    <li>Visionen, Strategien, Ziele oder Projekte formulieren und den Weg dahin definieren</li>
    <li>Gefahren erkennen und mögliche Sicherheitsmassnahmen analysieren, bewerten und bestimmen</li>
  </ul>
  <div class="abs body" style="left:318px;top:350px;width:147px">Not for Profit - Inhalte verfolgen und doch betriebswirtschaftlich agieren.</div>
  <div class="abs" style="left:482px;top:297px;width:100px;height:57px;background:linear-gradient(135deg,#0e2a3a,#4f8fa8 45%,#1b3d52)" role="img" aria-label="Blick durch eine Brille auf eine Stadt"></div>
</section>

<!-- Innen rechts -->
<section class="inner-right">
  <div class="abs offer-head" style="left:618px;top:90px">KONKRETE ANGEBOTE DAZU:</div>
  <div class="abs icon sq" style="left:618px;top:101px;width:25px;height:25px;background:#e9a35b" role="img" aria-label="Symbol Planungswerkzeuge"></div>
  <div class="abs offer-title" style="left:646px;top:101px">PROJEKTPLAN MIT KONKRETEN<br>MASSNAHMEN ENTWERFEN</div>
  <div class="abs body" style="left:618px;top:128px;width:125px">
    <p>Sie sollten eine Strategie entwickeln und auch formulieren, oder eine Jahresplanung und Ziele definieren? Projekte auf die Beine stellen oder für bestimmte Vorgaben konkrete Ziele formulieren?</p>
    <p>Ich plane und organisiere Strategieworkshops und moderiere diese als Aussenstehender. Ich plane und berechne mit Ihnen die Projektpläne und unterstütze Sie, dass diese dann auch realisiert werden.</p>
  </div>
  <div class="abs icon sq" style="left:757px;top:101px;width:25px;height:22px;background:#e46b5b" role="img" aria-label="Symbol zwei Mobilgeräte"></div>
  <div class="abs offer-title" style="left:785px;top:101px">NEUE WEGE DER<br>KOMMUNIKATION GESTALTEN</div>
  <div class="abs body" style="left:757px;top:128px;width:125px">
    <p>Sie haben Ihre eigene Kommunikationsagentur, die für Sie die konkrete Medienplanung betreibt, aber Sie wollen Ihre Kommunikation strategisch neu gestalten? Neue Medien, Ihren Webauftritt oder neue Zielgruppen ansprechen?</p>
    <p>Ich entwickle mit Ihnen entsprechende Kommunikationsstrategien oder auch ein konkretes Kommunikationsdesign (wie und wann kommunizieren wir mit wem?).</p>
  </div>
  <div class="abs band" style="left:600px;top:178px;width:300px">ENTWICKLUNGEN REALISIEREN</div>
  <div class="abs body" style="left:618px;top:202px;width:150px">Sie haben Strategien, Ziele, sonstige Vorgaben und müssen diese neben Ihrem Alltagsgeschäft umsetzten. Dafür suchen Sie Unterstützung eines</div>
  <ul class="abs body" style="left:618px;top:212px;width:150px">
    <li>Sparringpartners, mit dem Sie sich zu allgemeinen Herausforderungen oder konkreten Problemen austauschen wollen</li>
    <li>Moderators, der einen Strategieworkshop organisiert und auch dokumentiert</li>
    <li>Innovationsmanagers, der von aussen frischen Wind reinbringt</li>
    <li>Beraters mit der Kundenbrille, der die Kundensicht oder das Umfeld erforscht und hilft, neue Blickwinkel aber auch neue Lösungen hierfür zu entwickeln</li>
    <li>Kommunikators, der mit Stakeholdern in Kontakt tritt, bestehende Netzwerke nutzt und neue Netzwerke schafft</li>
    <li>erfahrenen Geschäftsführers, der hilft die Geschäftsstelle weiter zu professionalisieren und Finanzierungskonzepte zu entwickeln (inkl. Fundraising, Sponsoring und Crowdfunding)</li>
  </ul>
  <div class="abs" style="left:782px;top:203px;width:100px;height:57px;background:linear-gradient(135deg,#e08a5c,#d9774a 55%,#c9693f)" role="img" aria-label="Verbundene Drahtglieder eines Zauns"></div>
  <div class="abs offer-head" style="left:618px;top:272px">KONKRETE ANGEBOTE DAZU:</div>
  <div class="abs icon" style="left:618px;top:283px;width:25px;height:25px;background:#e9a35b" role="img" aria-label="Symbol Tachometer"></div>
  <div class="abs offer-title" style="left:646px;top:283px">FINANZIERUNGS-<br>KONZEPTE UND<br>KONKRETE<br>FINANZIERUNG</div>
  <div class="abs body" style="left:618px;top:312px;width:80px">
    <p>Sie haben viele Projektideen, aber wenig finanzielle Mittel, um diese umzusetzen? Wo und wie kommen Sie zu diesen?</p>
    <p>Ich zeige Ihnen die verschiedenen Möglichkeiten einer Finanzierung auf und unterstütze bei der Realisierung (Fundraising generell, Sponsoring, Crowdfunding, etc.).</p>
  </div>
  <svg class="abs" style="left:711px;top:283px" width="25" height="24" viewBox="0 0 25 24" role="img" aria-label="Symbol Organigramm"><rect x="9" y="1" width="7" height="6" fill="none" stroke="#555"/><path d="M12.5 7v5M3.5 12h18M3.5 12v4M12.5 12v4M21.5 12v4" stroke="#555" fill="none"/><rect x="1" y="16" width="5" height="5" fill="#e46b5b"/><rect x="10" y="16" width="5" height="5" fill="#e9a35b"/><rect x="19" y="16" width="5" height="5" fill="#e9a35b"/></svg>
  <div class="abs offer-title" style="left:739px;top:283px">PROFESSIONAL-<br>ISIERUNG VON<br>BACKOFFICE UND<br>GESCHÄFTSSTELLEN</div>
  <div class="abs body" style="left:711px;top:312px;width:80px">
    <p>Sie wollen die Administration, die Geschäftsprozesse, die ganze Geschäftsstelle optimieren? Ob Technik, IT oder CRM oder noch konkreter: Geschäftsreglement, Handbuch, etc.</p>
    <p>Ich helfe Ihnen in der Analyse, in der Zielsetzung und -findung. Auch im Finden passender Experten.</p>
  </div>
  <svg class="abs" style="left:803px;top:283px" width="20" height="26" viewBox="0 0 20 26" role="img" aria-label="Symbol Ortsmarke mit Person"><path d="M10 25C4 17 1 13 1 9a9 9 0 0 1 18 0c0 4-3 8-9 16z" fill="var(--accent)" stroke="#555" stroke-width=".8"/><circle cx="10" cy="9" r="5" fill="#fff" stroke="#555" stroke-width=".8"/></svg>
  <div class="abs offer-title" style="left:826px;top:283px">VR MANDATE UND<br>INTERIMSMANAGEMENT</div>
  <div class="abs body" style="left:803px;top:312px;width:80px">
    <p>Sie suchen nach einem Experten, der in Ihrer Organisation für einen Übergangszeitraum die Geschäftsführung übernimmt? Oder Sie suchen ein Verwaltungsratsmitglied, das mit seinem Fachwissen Ihren Verwaltungsrat unterstützt?</p>
    <p>Nach Absprache kann ich eine VR- oder eine befristete GF Funktion übernehmen.</p>
  </div>
</section>

<!-- Rückseite -->
<section class="back">
  <div class="abs back-photo" role="img" aria-label="Felsgipfel über Nebel und Wald unter blauem Himmel"></div>
  <h2 class="abs back-head h-display">WOFÜR STEHE ICH?</h2>
  <div class="abs body back-text" style="left:918px;top:118px;width:264px">Als Einzelperson stehe ich mit meiner Erfahrung, meinem Wissen und meiner Glaubwürdigkeit für Sie ein. Mein Zugang ist ein vernetzter und interdisziplinär. Ob nur in einem der oben angeführten Bereiche, oder in mehreren. Gerne unterstütze ich Sie.</div>
  <div class="abs h-display" style="left:918px;top:138px;width:264px;text-align:center;font-size:5px;font-weight:500">JRK – DAS OPTIMUM MACHEN… MIT ERFAHRUNG UND METHODEN KNOWHOW</div>
  <div class="abs body" style="left:918px;top:148px;width:264px;text-align:center">PERSÖNLICH. ZUVERLÄSSIG. DIREKT. INDIVIDUELL. DISKRET.<br>ICH VERSPRECHE NICHT ZU VIEL, DAS ABER HALTE ICH.</div>
  <div class="abs body" style="left:918px;top:168px;width:264px;color:#2b3f5a">Ich bringe langjährige Erfahrung als Geschäftsführer kleinerer Unternehmen oder Organisationen ein (z.B. Forschungs- und Beratungsunternehmen, Verband). Ebenso als Bereichsleiter Corporate Development grosser Unternehmen bis hin zu globalen Konzernen. In der profitorientierten wie auch in der Non Profit Wirtschaft. Meine ausgewiesenen Kompetenzen liegen in der Methodenkompetenz bei Strategie- und Organisationsentwicklung, in der Kommunikation sowie im Wissens- und Innovationsmanagement</div>
  <div class="abs contact">
    <div class="abs" style="left:28px;top:0;width:76px;height:54px;background:linear-gradient(180deg,#9bb0c4,#c9b3a0 55%,#5d6f86)" role="img" aria-label="Porträtfoto des Beraters"></div>
    <div class="abs contact-lines"><b>Dr. Jonas R. Keller</b><br>Am Lindenhof 8<br>CH-8004 Seefeld<br>+41 79 000 12 34<br>jonas@keller-beratung.net</div>
    <div class="abs brand">jrk</div>
  </div>
</section>
</body>
</html>
```